infographic - healing the addiction cycle

Please create a 3 slide infographic based on the three slides attached, as you can see they are builds on each other. I would love you to use pictures to complement the words and make it look beautiful. Please try to illustrate as much as possible i a looking for something really creative, clean and beautiful that articulates these concepts well.
My website is www.calmvessel.com.au so you can get an idea of branding and style.
This infographic will be used in training to teach new practitioners and clients how to heal their addictions.

Target Market(s)

Women aged 30 - 45

Industry/Entity Type

Professional Service

Font styles to use
Sans Serif

Colors

Designer to choose colors to be used in the design.

Requirements
Must have
• the blue color of my logo on it, i also like white
• Visual depictions not just words
• please look at my website to get an idea of style
Nice to have
• I would like it to be very clear, classy and as simple as possible
Should not have
• It needs to be neat not messy, symmetrical is better.

```html
<!DOCTYPE html>
<html lang="en">
<head>
<meta charset="utf-8">
<title>The Addiction Cycle Explained</title>
<link href="https://fonts.googleapis.com/css2?family=Cinzel:wght@400;600&family=Roboto+Condensed:wght@400;700&display=swap" rel="stylesheet">
<style>
  :root {
    --brand-blue: #29abe2;
    --tab-blue: #176b93;
    --slate: #3c404b;
    --ink: #2f3237;
    --white: #ffffff;
    --center-tint: #e9f5fc;
  }
  * { margin: 0; padding: 0; box-sizing: border-box; }
  html, body { width: 896px; height: 1200px; overflow: hidden; background: var(--white); }
  .sheet {
    position: relative; width: 896px; height: 1200px; overflow: hidden;
    background: var(--white);
    font-family: "Roboto Condensed", "Arial Narrow", sans-serif;
    color: var(--ink);
  }

  /* Header */
  .brand-mark {
    position: absolute; left: 247px; top: 30px; width: 96px; height: 96px;
    border: 4px solid var(--brand-blue); border-radius: 50%;
  }
  .brand-divider {
    position: absolute; left: 353px; top: 20px; width: 2px; height: 118px;
    background: var(--brand-blue);
  }
  .brand-name {
    position: absolute; left: 366px; top: 50px;
    font-size: 40px; font-weight: 400; color: var(--brand-blue); line-height: 1;
  }

  /* Title band */
  .title-band {
    position: absolute; left: 0; top: 156px; width: 896px; height: 60px;
    background: var(--brand-blue);
  }
  .title-band h1 {
    position: absolute; left: 112px; top: 6px;
    font-family: "Cinzel", serif; font-weight: 600; font-size: 40px;
    color: var(--white); letter-spacing: 1px; white-space: nowrap;
  }
  .step-tab { position: absolute; left: 8px; top: 126px; width: 100px; height: 136px; }
  .step-number {
    position: absolute; left: 8px; top: 138px; width: 88px; text-align: center;
    font-size: 70px; font-weight: 700; color: var(--white); line-height: 1;
  }

  /* Cycle */
  .cycle { position: absolute; left: 0; top: 0; width: 896px; height: 1200px; }
  .stage-label {
    position: absolute; font-weight: 700; color: var(--white);
    text-align: center; line-height: 0.98; white-space: nowrap;
    transform-origin: center;
  }
  .label-desire { left: 440px; top: 396px; width: 120px; font-size: 29px; }
  .label-negative { left: 568px; top: 492px; width: 150px; font-size: 22px; transform: rotate(-11deg); }
  .label-regret { left: 555px; top: 682px; width: 110px; font-size: 25px; }
  .label-judgment { left: 366px; top: 762px; width: 140px; font-size: 29px; }
  .label-act { left: 246px; top: 462px; width: 160px; font-size: 25px; transform: rotate(-40deg); }
  .label-relief { left: 243px; top: 655px; width: 100px; font-size: 29px; color: var(--brand-blue); transform: rotate(-12deg); }

  .center-art {
    position: absolute; left: 380px; top: 520px; width: 176px; height: 176px; border-radius: 50%;
    background: radial-gradient(circle, var(--center-tint) 0%, #ffffff 75%);
  }

  /* Annotations */
  .note { position: absolute; font-size: 18px; line-height: 1.1; }
  .note-blue { color: var(--brand-blue); }
  .note-craving { left: 542px; top: 227px; width: 340px; }
  .note-act { left: 8px; top: 357px; width: 202px; text-align: right; }
  .note-negative { left: 758px; top: 471px; width: 130px; }
  .note-relief { left: 20px; top: 743px; width: 170px; text-align: right; }
  .note-regret { left: 719px; top: 777px; width: 170px; }
  .note-regret p + p { margin-top: 18px; }
  .note-judgment { left: 392px; top: 909px; width: 320px; }

  /* Footer */
  .footer-band {
    position: absolute; left: 0; top: 1064px; width: 896px; height: 136px;
    background: var(--brand-blue);
  }
  .footer-name {
    position: absolute; left: 0; top: 30px; width: 896px; text-align: center;
    font-size: 64px; font-weight: 400; color: var(--white); line-height: 1;
  }
</style>
</head>
<body>
<main class="sheet">

  <header>
    <div class="brand-mark" aria-hidden="true"></div>
    <div class="brand-divider" aria-hidden="true"></div>
    <div class="brand-name">Inner Compass Healing</div>
  </header>

  <section class="title-band"><h1>The Addiction Cycle Explained</h1></section>
  <svg class="step-tab" viewBox="0 0 100 136" aria-hidden="true">
    <polygon points="88,0 100,30 88,30" fill="#0f4f6e"/>
    <polygon points="0,0 88,0 88,110 44,136 0,110" fill="var(--tab-blue)"/>
  </svg>
  <div class="step-number">1</div>

  <svg class="cycle" viewBox="0 0 896 1200" aria-hidden="true">
    <defs>
      <path id="blade" d="M110,0 Q199.2,-17.4 237.5,110.7 A262,262 0 0 1 22.8,261 Q114.7,163.8 55,95.3 A110,110 0 0 0 110,0 Z"/>
    </defs>
    <g transform="translate(468 608)">
      <use href="#blade" fill="var(--brand-blue)" transform="rotate(-116)"/>
      <use href="#blade" fill="var(--slate)" transform="rotate(-56)"/>
      <use href="#blade" fill="var(--brand-blue)" transform="rotate(4)"/>
      <use href="#blade" fill="var(--slate)" transform="rotate(64)"/>
      <use href="#blade" fill="var(--brand-blue)" transform="rotate(124)"/>
      <use href="#blade" fill="var(--slate)" transform="rotate(184)"/>
      <circle r="110" fill="#ffffff"/>
    </g>
    <g fill="#ffffff" transform="rotate(-12 293 672)">
      <ellipse cx="293" cy="676" rx="56" ry="25"/>
      <circle cx="266" cy="660" r="21"/>
      <circle cx="295" cy="650" r="25"/>
      <circle cx="324" cy="662" r="19"/>
      <circle cx="248" cy="680" r="15"/>
      <circle cx="338" cy="682" r="15"/>
    </g>
    <g stroke="var(--brand-blue)" stroke-width="2.5" fill="none">
      <polyline points="528,282 508,282 478,350"/>
      <polyline points="200,754 214,754 226,692"/>
      <polyline points="706,786 684,780"/>
    </g>
    <g stroke="var(--slate)" stroke-width="2.5" fill="none">
      <polyline points="222,368 236,368 284,432"/>
      <polyline points="748,480 736,480 714,496"/>
      <polyline points="381,920 364,920 350,850"/>
    </g>
    <g fill="var(--brand-blue)">
      <circle cx="528" cy="282" r="4.5"/>
      <circle cx="200" cy="754" r="4.5"/>
      <circle cx="706" cy="786" r="4.5"/>
    </g>
    <g fill="var(--slate)">
      <circle cx="222" cy="368" r="4.5"/>
      <circle cx="748" cy="480" r="4.5"/>
      <circle cx="381" cy="920" r="4.5"/>
    </g>
  </svg>

  <div class="center-art" role="img" aria-label="Illustration of a joyful leaping person in a suit, celebrating"></div>

  <div class="stage-label label-desire">Desire/<br>Craving</div>
  <div class="stage-label label-negative">Negative<br>Thoughts,<br>Physical<br>Pain, Heavy<br>emotions</div>
  <div class="stage-label label-regret">Regret/<br>Guilt/<br>Shame<br>Sadness</div>
  <div class="stage-label label-judgment">Self<br>Judgment</div>
  <div class="stage-label label-act">Act on the<br>addiction</div>
  <div class="stage-label label-relief">Relief</div>

  <p class="note note-blue note-craving">Mental and emotional pain becomes physically unbearable and our unconscious desire to sooth or suppress it creates the craving/desire to overcome the pain through the addictive behavior</p>
  <p class="note note-act">When can no longer hold back our desire/craving so we commit self abuse through addictive behaviour e.g. drugs, alcohol, food, gambling, exercise etc..</p>
  <p class="note note-negative">Physical ( ie: nausea, anxiety, depression) and mental reaction (ie: Negative self talk) to the emotional response</p>
  <p class="note note-blue note-relief">We experience a brief relief from emotion, mental and physical pain</p>
  <div class="note note-blue note-regret">
    <p>This is the emotional reaction to self judgment</p>
    <p>This is often experienced on an unconscious level</p>
  </div>
  <p class="note note-judgment">We now judge ourselves for carrying out the addictive behavior:<br>I’m not good enough,<br>I’m a failure<br>I am weak<br>This process is often unconscious</p>

  <footer class="footer-band"><div class="footer-name">Calm Vessel</div></footer>

</main>
</body>
</html>
```